Real Estate Flyer

Hi - I am assisting a relative to sell a unit. I am looking to have a two page flyer designed (configured as a single page with back to back printing). I have uploaded two samples to give you an idea of the look and feel - one which relates to this property when originally purchased, the other for a different property.
The flyer should includes several key photos on the front along with the wording. The rear should include any secondary photos along with the floor plan.
The flyer should be close to A4 size.

Updates
Hi,
Industry/Entity Type
Real Estate
Look and feel
Each slider illustrates characteristics of the customer's brand and the style your logo design should communicate.

```html
<!DOCTYPE html>
<html lang="en">
<head>
<meta charset="utf-8">
<title>Oversized apartment in a lifestyle location</title>
<link href="https://fonts.googleapis.com/css2?family=Open+Sans:wght@400;600;700&display=swap" rel="stylesheet">
<style>
:root{
  --navy:#1d3f73;
  --ink:#2b2b2b;
  --muted:#6b6f75;
  --band:#e8edf3;
  --page:#ffffff;
  --frame:#d9dcdf;
}
*{box-sizing:border-box;margin:0;padding:0}
html,body{width:849px;height:1200px;overflow:hidden;background:var(--page)}
body{font-family:"Open Sans",Arial,sans-serif;color:var(--ink);position:relative}
.backdrop{position:absolute;inset:0;background:linear-gradient(180deg,#c9ccd0 0%,#eceef0 45%,#f6f7f8 60%,#e3e5e8 100%)}
.photo{position:absolute;border:3px solid #fff;box-shadow:0 2px 8px rgba(0,0,0,.25)}
.photo-exterior{left:118px;top:0;width:708px;height:330px;background:linear-gradient(180deg,#3e7fc4 0%,#7fb0de 35%,#c58a5c 60%,#3bb6d6 85%,#1d8fb8 100%)}
.photo-interior{left:22px;top:238px;width:375px;height:290px;background:linear-gradient(160deg,#f1e8d8 0%,#d9c7a6 50%,#b98c5d 100%)}
.photo-pool{left:397px;top:330px;width:429px;height:198px;background:linear-gradient(180deg,#9fb9cf 0%,#4fc1dc 45%,#1f9ac0 100%)}
.sheet{position:absolute;left:22px;right:22px;top:540px;bottom:22px;background:rgba(255,255,255,.93)}
.features{position:absolute;right:28px;top:565px;display:flex;gap:22px;align-items:center;font-size:22px;color:var(--muted)}
.features span{display:flex;align-items:center;gap:8px}
.features svg{width:36px;height:24px;stroke:var(--muted);fill:none;stroke-width:2}
.address{position:absolute;right:30px;top:665px;font-size:21px;color:var(--navy);font-weight:600}
.address strong{font-weight:700}
.headline{position:absolute;left:22px;right:22px;top:698px;height:40px;background:var(--band);padding:4px 18px;font-size:24px;font-weight:700;color:var(--navy)}
.intro{position:absolute;left:40px;right:40px;top:748px;font-size:14.5px;line-height:1.55;text-indent:40px;text-align:justify}
.highlights{position:absolute;left:40px;top:860px;width:360px;list-style:none;font-size:13.5px;line-height:1.5}
.highlights li{padding-left:18px;position:relative;margin-bottom:5px}
.highlights li::before{content:"";position:absolute;left:2px;top:8px;width:6px;height:6px;border-radius:50%;background:var(--navy)}
.details{position:absolute;left:425px;top:860px;width:390px;font-size:13.5px;line-height:1.5}
.details p{margin-bottom:6px}
.details .gap{margin-top:14px}
.details .label{font-weight:600}
</style>
</head>
<body>
<div class="backdrop" role="img" aria-label="Faded architectural photograph of apartment buildings behind the flyer"></div>
<div class="photo photo-exterior" role="img" aria-label="Photograph of the apartment tower with balconies and city skyline under blue sky"></div>
<div class="photo photo-pool" role="img" aria-label="Photograph of the rooftop swimming pool and sun terrace"></div>
<div class="photo photo-interior" role="img" aria-label="Photograph of the bright open-plan living room opening onto the terrace"></div>
<div class="sheet"></div>

<div class="features">
  <span><svg viewBox="0 0 36 24"><path d="M3 4v16M3 14h30v6M3 10h8v4M11 10h18a4 4 0 0 1 4 4"/></svg>2</span>
  <span><svg viewBox="0 0 36 24"><path d="M3 12h30M5 12v4a5 5 0 0 0 5 5h16a5 5 0 0 0 5-5v-4M8 12V5a2 2 0 0 1 4 0"/></svg>1</span>
  <span><svg viewBox="0 0 36 24"><path d="M4 17v-5l4-6h20l4 6v5zM4 17v3h4v-3M28 17v3h4v-3"/><circle cx="10" cy="13" r="1.5"/><circle cx="26" cy="13" r="1.5"/></svg>1</span>
</div>

<div class="address">12/40-48 Harbour Lane, <strong>LINDEN HEIGHTS</strong></div>
<h1 class="headline">Oversized apartment in a lifestyle location</h1>

<p class="intro">Peacefully positioned on the 5th floor of a refurbished security building, this superbly spacious residence combines modern, low maintenance apartment living with inviting prospects for the entertainer. Boasting a huge full-width terrace on-tile, its sought-after setting in the heart of Linden Heights offers the ultimate in lifestyle and convenience.</p>

<ul class="highlights">
  <li>Expansive open plan living and dining area</li>
  <li>Terrace features city and Botany Bay glimpses</li>
  <li>Kitchen updated with Corvella gas appliances</li>
  <li>Built-ins in both bedrooms, fully tiled bathrooms</li>
  <li>Internal laundry, secure parking, lift, outdoor pool and gymnasium</li>
  <li>Steps to station, Marlowe Plaza and Rosehill Park</li>
</ul>

<div class="details">
  <p><span class="label">Water Rates:</span> To be provided on finalizing design</p>
  <p><span class="label">Council Rates:</span> To be provided on finalizing design</p>
  <p><span class="label">Strata Rates:</span> To be provided on finalizing design</p>
  <p class="gap"><span class="label">Estimated Market Rent:</span> $700.00 p/w</p>
  <p class="gap"><span class="label">Inspect:</span> Sat 10:45 – 11:30; Wed 12:00 – 12:30</p>
  <p class="gap"><span class="label">Contact:</span> <strong>Daniel Hartley (Assisting owner in Private Sale) – 0400 555 182</strong></p>
</div>
</body>
</html>
```